Regenerative Medicine clinic needs PRP (Platelet Rich Plasma) marketing Tri-Fold Brochure

We are a physical medicine/Regnerative medicine clinic called 'Corevale Medical Group' out of Dallas, TX. We provide a Regenerative Medicine injection called 'Platelet Rich Plasma' or 'PRP' for patients with acute and chronic joint pain and joint conditions. We would like a brochure that outlines what PRP is, who is for, what it treats, and how it would benefit patients in a simplistic way. Pictures appreciated!

Target Market(s)

Older people with joint issues, and younger athletes

Industry/Entity Type

Medical, Regenerative Medicine

Font styles to use
Sans Serif

Colors
F0912C
F2A743
F7CA91
FBE8D2
FDF5EE

Requirements
Must have
• Logo and website and phone number - www.corevaleclinic.example, 214-555-0187

```html
<!DOCTYPE html>
<html lang="en">
<head>
<meta charset="utf-8">
<title>Corevale Medical Group – PRP Tri-Fold Brochure</title>
<link rel="stylesheet" href="https://fonts.googleapis.com/css2?family=Montserrat:wght@400;600;700;800&family=Open+Sans:wght@400;600&display=swap">
<style>
  :root{
    --orange:#F0912C;
    --orange-mid:#F2A743;
    --peach:#F7CA91;
    --cream:#FBE8D2;
    --paper:#FDF5EE;
    --white:#ffffff;
    --ink:#3a3a3a;
    --ink-soft:#6b6b6b;
    --charcoal:#3d3d3f;
    --backdrop:#e6e6e6;
  }
  *{box-sizing:border-box;margin:0;padding:0}
  html,body{width:865px;height:1200px;overflow:hidden;background:var(--backdrop)}
  body{font-family:"Open Sans",Arial,sans-serif;color:var(--ink);position:relative}

  .spread{position:absolute;left:20px;width:825px;height:560px;background:var(--white);display:flex;box-shadow:0 2px 10px rgba(0,0,0,.12);overflow:hidden}
  .spread--outside{top:20px}
  .spread--inside{top:620px}
  .panel{position:relative;width:275px;height:100%;overflow:hidden}
  .panel + .panel{border-left:1px solid #eee}

  h2,h3,.title{font-family:"Montserrat",Arial,sans-serif}

  /* Logo */
  .logo{display:flex;align-items:center;gap:8px}
  .logo__dot{width:22px;height:22px;border-radius:50%;background:var(--orange);flex:none}
  .logo__name{font-family:"Montserrat",Arial,sans-serif;font-weight:700;font-size:14px;color:var(--orange);line-height:1.15}

  /* Outside – left panel */
  .media{position:absolute}
  .media--spine{left:0;top:0;width:275px;height:200px;background:radial-gradient(circle at 60% 55%,#f7a24a 0,#c05a3a 12%,#2b3f8f 38%,#121c4a 100%)}
  .what-prp__shape{position:absolute;left:0;top:0;width:275px;height:560px}
  .what-prp__text{position:absolute;left:22px;top:240px;width:175px;color:var(--white)}
  .what-prp__text h2{font-size:18px;font-weight:800;margin-bottom:12px}
  .what-prp__text p{font-size:11px;line-height:1.6}

  /* Outside – middle panel */
  .ribbon{position:absolute;left:0;top:30px}
  .contact{position:absolute;left:0;right:0;top:190px;display:flex;flex-direction:column;align-items:center;text-align:center;gap:10px}
  .contact .logo__name{font-size:15px}
  .contact__ask{margin-top:40px;font-family:"Montserrat",Arial,sans-serif;font-weight:700;font-size:15px;color:var(--orange);line-height:1.3}
  .contact__label{font-size:12px;color:var(--ink-soft)}
  .contact__phone{display:flex;align-items:center;gap:6px;font-family:"Montserrat",Arial,sans-serif;font-weight:700;font-size:15px;color:var(--ink)}
  .contact__web{font-size:11px;color:var(--ink-soft)}

  /* Outside – right panel */
  .cover__band{position:absolute;left:0;top:0;width:275px;height:70px;background:var(--orange);display:flex;align-items:center;justify-content:center}
  .cover__band h1{font-family:"Montserrat",Arial,sans-serif;font-weight:800;font-size:17px;color:var(--white);letter-spacing:.5px;text-align:center;line-height:1.2}
  .cover__sub{position:absolute;left:30px;right:30px;top:95px;text-align:center}
  .cover__sub h2{font-size:13px;font-weight:700;color:var(--ink);margin-bottom:8px}
  .cover__sub p{font-size:11px;line-height:1.5;color:var(--orange);font-weight:600}
  .media--consult{left:40px;top:185px;width:195px;height:150px;border-radius:50%;background:radial-gradient(circle,#dfe9f5 0,#c7d8ee 55%,var(--cream) 100%)}
  .cover__logo{position:absolute;left:0;right:0;top:380px;display:flex;justify-content:center}
  .cover__wave{position:absolute;left:0;bottom:0;width:275px;height:90px}

  /* Inside */
  .copy{position:absolute;left:22px;right:22px}
  .copy h2{font-size:15px;font-weight:800;color:var(--orange);margin-bottom:8px}
  .copy h3{font-size:12px;font-weight:700;color:var(--ink);margin:12px 0 6px}
  .copy p{font-size:10.5px;line-height:1.6;color:var(--ink-soft)}
  .copy--what{top:34px}
  .media--treatment{left:22px;top:300px;width:231px;height:185px;background:linear-gradient(160deg,var(--paper),#dfe7ee 55%,var(--cream))}
  .footer-band{position:absolute;left:0;bottom:0;width:275px;height:45px;background:var(--charcoal)}
  .copy--about{top:34px}
  .about__logo{position:absolute;left:22px;bottom:40px}
  .corner{position:absolute;left:0;top:0}
  .copy--benefits{top:40px;left:40px}
  .benefits{list-style:none}
  .benefits li{display:flex;align-items:center;gap:8px;font-size:11px;color:var(--ink);margin-bottom:7px}
  .benefits svg{flex:none}
  .media--knee{left:0;top:220px;width:275px;height:340px;background:linear-gradient(135deg,#f3ece6 0,#d9dfe8 40%,#eed9c6 75%,#c9a58a 100%)}
</style>
</head>
<body>

<section class="spread spread--outside" aria-label="Brochure outside">
  <article class="panel panel--what-prp">
    <svg class="what-prp__shape" viewBox="0 0 275 560" aria-hidden="true">
      <path d="M0 200 L275 200 C225 320 235 460 150 560 L0 560 Z" fill="var(--orange)"/>
      <path d="M275 200 C225 320 235 460 150 560 L175 560 C255 460 250 330 275 250 Z" fill="var(--peach)"/>
    </svg>
    <div class="media media--spine" role="img" aria-label="Photo of a human back with a glowing spine showing joint pain"></div>
    <div class="what-prp__text">
      <h2>What PRP is</h2>
      <p>Platelet rich plasma is made from your own blood. Platelets are concentrated and injected into the injured joint to support natural healing and ease pain.</p>
    </div>
  </article>

  <article class="panel panel--contact">
    <svg class="ribbon" width="80" height="40" viewBox="0 0 80 40" aria-hidden="true">
      <path d="M0 0 H80 L65 20 L80 40 H0 Z" fill="var(--orange)"/>
    </svg>
    <div class="contact">
      <div class="logo"><span class="logo__dot"></span><span class="logo__name">Corevale Medical Group</span></div>
      <p class="contact__ask">Request an<br>Appointment Today?</p>
      <p class="contact__label">Give us a call:</p>
      <p class="contact__phone">
        <svg width="16" height="16" viewBox="0 0 24 24" aria-hidden="true"><path fill="var(--orange)" d="M6.6 10.8a15.1 15.1 0 0 0 6.6 6.6l2.2-2.2a1 1 0 0 1 1-.25 11.4 11.4 0 0 0 3.6.57 1 1 0 0 1 1 1V20a1 1 0 0 1-1 1A17 17 0 0 1 3 4a1 1 0 0 1 1-1h3.5a1 1 0 0 1 1 1c0 1.25.2 2.45.57 3.57a1 1 0 0 1-.25 1z"/></svg>
        214-555-0187
      </p>
      <p class="contact__web">www.corevaleclinic.example</p>
    </div>
  </article>

  <article class="panel panel--cover">
    <div class="cover__band"><h1>PLATELET RICH<br>PLASMA</h1></div>
    <div class="cover__sub">
      <h2>A Regenerative Medicine Solution</h2>
      <p>To help patients with acute and chronic joint pain and joint conditions</p>
    </div>
    <div class="media media--consult" role="img" aria-label="Illustration of a doctor giving a PRP injection to a patient"></div>
    <div class="cover__logo"><div class="logo"><span class="logo__dot"></span><span class="logo__name">Corevale Medical Group</span></div></div>
    <svg class="cover__wave" viewBox="0 0 275 90" preserveAspectRatio="none" aria-hidden="true">
      <path d="M0 40 C90 0 180 70 275 20 V90 H0 Z" fill="var(--peach)"/>
      <path d="M0 55 C90 20 180 85 275 40 V90 H0 Z" fill="var(--orange)"/>
    </svg>
  </article>
</section>

<section class="spread spread--inside" aria-label="Brochure inside">
  <article class="panel panel--what">
    <div class="copy copy--what">
      <h2>What it is</h2>
      <p>PRP uses a small sample of your blood. It is spun to concentrate platelets, which carry growth factors. A quick injection delivers them to the joint to help tissue repair.</p>
      <h3>Who is it for?</h3>
      <p>Older adults with joint wear and younger athletes with sports injuries.</p>
    </div>
    <div class="media media--treatment" role="img" aria-label="Illustration of a doctor showing a report to a patient resting in bed"></div>
    <div class="footer-band"></div>
  </article>

  <article class="panel panel--about">
    <div class="copy copy--about">
      <h2>About Corevale Medical Group</h2>
      <p>Corevale Medical Group is a physical and regenerative medicine clinic in Dallas, TX. Our team treats acute and chronic joint pain with care built around each patient.</p>
      <h3>What it treats</h3>
      <p>Knee, shoulder, hip and elbow pain, tendon and ligament injuries, and arthritis.</p>
    </div>
    <div class="about__logo"><div class="logo"><span class="logo__dot"></span><span class="logo__name">Corevale Medical Group</span></div></div>
  </article>

  <article class="panel panel--benefits">
    <svg class="corner" width="60" height="60" viewBox="0 0 60 60" aria-hidden="true"><path d="M0 0 H60 L0 60 Z" fill="var(--orange)"/></svg>
    <div class="copy copy--benefits">
      <h2>Benefits</h2>
      <ul class="benefits">
        <li><svg width="12" height="12" viewBox="0 0 12 12" aria-hidden="true"><path d="M2 6 L5 9 L10 3" stroke="var(--orange)" stroke-width="2" fill="none"/></svg>Uses your own blood</li>
        <li><svg width="12" height="12" viewBox="0 0 12 12" aria-hidden="true"><path d="M2 6 L5 9 L10 3" stroke="var(--orange)" stroke-width="2" fill="none"/></svg>Minimally invasive</li>
        <li><svg width="12" height="12" viewBox="0 0 12 12" aria-hidden="true"><path d="M2 6 L5 9 L10 3" stroke="var(--orange)" stroke-width="2" fill="none"/></svg>Little to no downtime</li>
        <li><svg width="12" height="12" viewBox="0 0 12 12" aria-hidden="true"><path d="M2 6 L5 9 L10 3" stroke="var(--orange)" stroke-width="2" fill="none"/></svg>Supports natural healing</li>
      </ul>
    </div>
    <div class="media media--knee" role="img" aria-label="Photo of a person in a striped shirt holding a painful knee"></div>
  </article>
</section>

</body>
</html>
```